Pellu an Organic Supplement Brand

A product label for a Supplement Brand. Company is called "Pellu" and the tagline is "Wellness Grows Together". Their will be multiple products such as capsules, liquids, powders, etc. Lets focus on Vitamin C capsules, but if you want to play around with color pallets and or multiple supplements that would be great. Want it to be a simple, clean and sophisticated design that looks fresh and stands out. This product has high quality organic ingredients. Attached is label specifications as well as an image for stock language for left and right side of label for reference and some sample products. Parts can be omitted, added or mixed and matched as needed.
Moms
Health and Wellness

```html
<!DOCTYPE html>
<html lang="en">
<head>
<meta charset="utf-8">
<title>Pellu Vitamin C Label</title>
<link rel="stylesheet" href="https://fonts.googleapis.com/css2?family=Montserrat:wght@400;500;600;700&display=swap">
<style>
  :root {
    --bg: #cfcfcf;
    --label-white: #f4f4f3;
    --yellow: #e6be22;
    --yellow-deep: #d9ac10;
    --yellow-soft: #f3dc7a;
    --ink: #3a3a3c;
    --ink-dark: #2e2b28;
  }
  * { margin: 0; padding: 0; box-sizing: border-box; }
  html, body {
    width: 1200px; height: 1200px; overflow: hidden;
    background: var(--bg);
    font-family: "Montserrat", sans-serif;
  }
  .label {
    position: absolute; left: 120px; top: 70px;
    width: 960px; height: 1060px;
    background: var(--label-white);
    overflow: hidden;
  }
  .label__top-band {
    position: absolute; left: 0; top: 0; width: 100%; height: 560px;
    background: linear-gradient(100deg, var(--yellow-deep) 0%, var(--yellow) 55%, #efcd3c 100%);
  }
  .label__wave { position: absolute; left: 0; top: 0; width: 960px; height: 1060px; }
  .brand { position: absolute; left: 66px; top: 96px; }
  .brand__name {
    font-weight: 600; font-size: 60px; letter-spacing: 0;
    color: var(--ink); line-height: 1;
  }
  .brand__tagline {
    margin-top: 12px;
    font-weight: 500; font-size: 22px; color: var(--ink);
  }
  .category { position: absolute; left: 62px; top: 490px; line-height: 1; }
  .category__kind { font-weight: 400; font-size: 44px; color: var(--yellow-soft); }
  .category__type { margin-top: 34px; font-weight: 700; font-size: 44px; color: var(--ink-dark); }
  .product-name {
    position: absolute; left: 790px; top: 70px;
    transform-origin: 0 0; transform: rotate(90deg);
    font-weight: 600; font-size: 140px; color: var(--ink);
    line-height: 1; white-space: nowrap; letter-spacing: -2px;
  }
  .count { position: absolute; left: 44px; top: 895px; display: flex; align-items: center; gap: 8px; }
  .count__icon { width: 34px; height: 78px; }
  .count__number { font-weight: 700; font-size: 54px; color: var(--ink-dark); line-height: 1; }
  .count__unit { font-weight: 500; font-size: 16px; color: var(--ink-dark); line-height: 1; margin-top: 2px; }
  .dose {
    position: absolute; left: 758px; top: 930px;
    font-weight: 500; font-size: 26px; letter-spacing: 5px; color: var(--label-white);
  }
  .form {
    position: absolute; left: 0; width: 960px; top: 1012px; padding-left: 222px;
    font-weight: 500; font-size: 28px; letter-spacing: 6px; color: var(--yellow-soft);
  }
</style>
</head>
<body>
  <div class="label">
    <div class="label__top-band"></div>
    <svg class="label__wave" viewBox="0 0 960 1060" aria-hidden="true">
      <defs>
        <linearGradient id="waveFill" x1="0" y1="0" x2="1" y2="0">
          <stop offset="0" stop-color="#e3b91c"/>
          <stop offset="1" stop-color="#efcd3c"/>
        </linearGradient>
      </defs>
      <path d="M0 992 L520 992 C610 992 610 900 720 900 L960 900 L960 1060 L0 1060 Z" fill="url(#waveFill)"/>
    </svg>

    <div class="brand">
      <div class="brand__name">Pellu</div>
      <div class="brand__tagline">Wellness Grows Together</div>
    </div>

    <div class="category">
      <div class="category__kind">DIETARY</div>
      <div class="category__type">SUPLEMENT</div>
    </div>

    <div class="product-name">Vitamin C</div>

    <div class="count">
      <svg class="count__icon" viewBox="0 0 34 78" aria-hidden="true">
        <rect x="2" y="2" width="30" height="74" rx="15" fill="none" stroke="#e6be22" stroke-width="3.5"/>
        <path d="M2 39 L32 39 L32 61 A15 15 0 0 1 2 61 Z" fill="#e6be22"/>
        <path d="M10 14 A8 8 0 0 1 18 9" fill="none" stroke="#e6be22" stroke-width="3" stroke-linecap="round"/>
      </svg>
      <div>
        <div class="count__number">180</div>
        <div class="count__unit">CAPSULES</div>
      </div>
    </div>

    <div class="dose">500 MG</div>
    <div class="form">VEGETARIAN CAPSULES</div>
  </div>
</body>
</html>
```